Oakhaven Construction Need an information and interactive website with client portal. We have ou

Need to have a client log in screen for work orders and estimate requests.
Nice informational landing page.

Oakhaven is a full service general contractor servicing apartment complexes;
maintenance of grounds and apartments - remodeling and construction.

Design Specifics: We are pretty open here. Some good examples are
www.marrowpeakbuilders.com , tovelresidence.com and www.quillbyworksite.com

For the site we need:
Homepage - to explain services
Roofing page
Apartment Page
Client Portal - where clients can set up accounts to set up work/estimate request that will be routed to our email

--Will need coding, plan to host site on Wordpress

Target Market(s)

Multi family, Residential and commercial clients

Industry/Entity Type

Construction

Coding

Coded - Design and coding required

Number of Pages Required

3 page

Font styles to use
Serif

Requirements
Must have
• Client portal
Nice to have
• Not sure. please advise

```html
<!DOCTYPE html>
<html lang="en">
<head>
<meta charset="utf-8">
<title>Oakhaven Construction</title>
<link href="https://fonts.googleapis.com/css2?family=Lato:wght@300;400;700;900&display=swap" rel="stylesheet">
<style>
:root{
  --red:#b5121b;
  --navy:#0b0c80;
  --ink:#1b1b1b;
  --text:#444;
  --muted:#777;
  --line:#e3e3e3;
  --black:#1a1a1a;
  --white:#fff;
}
*{box-sizing:border-box;margin:0;padding:0}
html,body{width:1200px;height:2256px;overflow:hidden}
body{position:relative;background:var(--white);font-family:'Lato',sans-serif;color:var(--text)}
.abs{position:absolute}

/* top bar */
.topbar{left:0;top:0;width:1200px;height:24px;display:flex}
.topbar .seg{height:24px;display:flex;align-items:center;color:var(--white);font-size:11px}
.seg-mail{width:399px;background:var(--red);padding-left:172px;gap:6px}
.seg-social{width:399px;background:var(--black);justify-content:center;gap:14px}
.seg-phone{width:402px;background:var(--navy);justify-content:flex-end;padding-right:172px;gap:6px}
.dot{width:9px;height:9px;border-radius:50%;background:var(--white);display:inline-block}
.dot.dark{background:var(--ink)}

/* header */
.brand{left:172px;top:44px;display:flex;align-items:center;gap:12px}
.brand-mark{width:40px;height:40px;background:var(--red)}
.brand-name{font-weight:900;font-size:27px;color:var(--navy);letter-spacing:.5px;line-height:1;text-transform:uppercase}
.nav{top:66px;left:626px;display:flex;align-items:center;font-size:12px;font-weight:700;color:var(--ink)}
.nav a{color:inherit;text-decoration:none;position:relative}
.nav .sep{width:4px;height:4px;border-radius:50%;background:var(--red);margin:0 16px}
.nav a.active{color:var(--navy)}
.nav a.active::after{content:"";position:absolute;left:0;right:0;bottom:-6px;height:2px;background:var(--navy)}

/* hero */
.hero{left:0;top:132px;width:1200px;height:390px;background:linear-gradient(100deg,#b8c3cc 0%,#d3d6d4 30%,#8aa4c3 60%,#44678f 80%,#c7a96a 100%)}
.hero-card{left:259px;top:205px;width:293px;height:244px;background:rgba(245,245,245,.86);text-align:center;padding-top:12px}
.hero-card h1{font-size:22px;font-weight:400;color:var(--ink);line-height:27px}
.hero-card .rule{height:2px;background:var(--red);margin:10px 0 12px}
.hero-card p{font-size:10.5px;line-height:18px;color:#555;padding:0 26px}
.btn-red{display:inline-block;background:var(--red);color:var(--white);font-size:15px;padding:8px 0;width:173px;margin-top:14px;text-transform:uppercase}

/* section titles */
.sec-title{left:170px;width:857px;display:flex;align-items:center;gap:26px}
.sec-title h2{font-size:23px;font-weight:400;color:var(--ink);position:relative;white-space:nowrap}
.sec-title h2::after{content:"";position:absolute;left:44px;bottom:-8px;width:74px;height:2px;background:var(--red)}
.sec-title .track{flex:1;height:5px;border-top:1px solid var(--line);border-bottom:1px solid var(--line)}

/* service process */
.steps{left:170px;top:609px;width:857px;height:121px;display:flex;border:1px solid var(--line)}
.step{flex:1;display:flex;flex-direction:column;align-items:center;justify-content:center;gap:14px;font-size:13px;color:var(--ink);border-right:1px solid var(--line)}
.step:last-child{border-right:0}
.step .icon{width:50px;height:50px;border-radius:50%;border:2px solid #e6e6e6;display:flex;align-items:center;justify-content:center}
.step.active{background:var(--black);color:var(--white)}
.step.active .icon{background:var(--red);border:3px solid var(--white)}

/* services */
.intro{left:170px;width:857px;font-size:10px;line-height:22.5px;color:#333}
.svc{top:893px;width:202px;height:210px}
.svc .photo{width:100%;height:100%}
.svc span{position:absolute;left:0;right:0;bottom:8px;text-align:center;color:var(--white);font-size:13.5px;font-weight:700}
.chev{width:14px;height:22px}

/* about */
.feature{top:1282px;width:260px}
.feature h3{font-size:17px;font-weight:400;color:var(--red);margin-bottom:6px}
.feature p{font-size:10px;line-height:22.5px;color:#333}

/* recent projects */
.band{left:0;top:1452px;width:1200px;height:319px;background:linear-gradient(180deg,#4a4aa8 0%,#3d3d98 55%,#25246e 100%)}
.proj{top:1482px;width:271px;height:259px}
.proj .photo{position:absolute;inset:0}
.proj .frame{position:absolute;left:24px;top:24px;right:24px;bottom:24px;border:1.5px solid #222}
.proj h4{position:absolute;left:0;right:0;top:112px;text-align:center;font-size:21px;font-weight:700;color:#111}

/* cta */
.cta{left:0;top:1809px;width:1200px;height:65px;background:var(--red);display:flex;align-items:center;justify-content:center;gap:40px}
.cta .q{font-size:22px;color:var(--white);font-weight:700}
.cta .q u{color:var(--black);font-weight:700}
.btn-black{background:var(--black);color:var(--white);font-size:22px;padding:4px 14px}

/* contact */
.box{border:1px solid var(--line)}
.info{left:170px;top:1960px;width:217px;height:188px;text-align:center;font-size:11px;color:#222;padding-top:16px;line-height:32px}
.info .socials{display:flex;justify-content:center;gap:14px;margin-top:6px}
.map{left:406px;top:1960px;width:384px;height:188px;background:linear-gradient(135deg,#e9e4d6,#f0e6b6 45%,#c9d6c2 70%,#b7c9dc)}
.field{border:1px solid #d6d6d6;font-size:10px;color:#444;padding:4px 6px}
.field i{color:var(--red);font-style:normal}
.submit{left:810px;top:2127px;width:74px;height:21px;background:var(--navy);color:var(--white);font-size:12px;display:flex;align-items:center;justify-content:center}

/* footer */
.footer{left:0;top:2185px;width:1200px;height:71px;background:var(--black);color:#ddd;text-align:center}
.footer nav{display:flex;justify-content:center;gap:30px;font-size:10px;padding-top:16px}
.footer nav .active{color:var(--red)}
.footer p{font-size:10px;margin-top:14px}
</style>
</head>
<body>

<div class="abs topbar">
  <div class="seg seg-mail">
    <svg width="12" height="9" viewBox="0 0 12 9"><rect x=".5" y=".5" width="11" height="8" fill="none" stroke="#fff"/><path d="M.5 .5 6 5 11.5 .5" fill="none" stroke="#fff"/></svg>
    info@oakhavenbuild.com
  </div>
  <div class="seg seg-social"><span class="dot"></span><span class="dot"></span><span class="dot"></span><span class="dot"></span><span class="dot"></span></div>
  <div class="seg seg-phone">
    <svg width="10" height="10" viewBox="0 0 10 10"><path d="M2 0 4 2.5 3 3.6Q4.2 6 6.4 7L7.5 6 10 8 8.6 10Q2 9 0 1.4Z" fill="#fff"/></svg>
    (012)-555-0147
  </div>
</div>

<div class="abs brand">
  <span class="brand-mark"></span>
  <span class="brand-name">Oakhaven Construction</span>
</div>

<nav class="abs nav">
  <a class="active">Home</a><span class="sep"></span>
  <a>Roofing</a><span class="sep"></span>
  <a>Apartment</a><span class="sep"></span>
  <a>Client Portal</a><span class="sep"></span>
  <a>Contact Us</a>
</nav>

<div class="abs hero" role="img" aria-label="Builder holding a yellow hard hat and rolled plans in front of a building under construction"></div>
<div class="abs hero-card">
  <h1>Home Improvements<br>And Remodeling</h1>
  <div class="rule"></div>
  <p>Morbi at ex porta, cursus magna nec, laoreet purus. Pellentesque tortor augue, finibus non massa a, sollicitudin facilisis dui.Morbi at ex porta, cursus magna nec, laoreet purus. Pellentesque tortor augue, finibus non massa a, sollicitudin facilisis dui.</p>
  <span class="btn-red">Client Portal</span>
</div>

<div class="abs sec-title" style="top:554px"><h2>Service Process</h2><span class="track"></span></div>
<div class="abs steps">
  <div class="step">
    <span class="icon"><svg width="14" height="14" viewBox="0 0 14 14"><circle cx="7" cy="4" r="3.2" fill="#999"/><path d="M1 14Q1 8 7 8T13 14Z" fill="#999"/></svg></span>
    Communication
  </div>
  <div class="step active">
    <span class="icon"><svg width="18" height="12" viewBox="0 0 18 12"><path d="M1 6Q9-3 17 6Q9 15 1 6Z" fill="#fff"/><circle cx="9" cy="6" r="2.4" fill="#b5121b"/></svg></span>
    Project Overview
  </div>
  <div class="step">
    <span class="icon"><svg width="13" height="16" viewBox="0 0 13 16"><path d="M1 1h8l3 3v11H1Z" fill="none" stroke="#999" stroke-width="1.2"/><path d="M3.5 7h6M3.5 9.5h6M3.5 12h6" stroke="#999"/></svg></span>
    Agreement
  </div>
  <div class="step">
    <span class="icon"><svg width="12" height="17" viewBox="0 0 12 17"><rect x="1" y="1" width="10" height="15" rx="1.5" fill="none" stroke="#999" stroke-width="1.2"/><rect x="3" y="3.5" width="6" height="8" fill="#bbb"/><circle cx="6" cy="13.7" r=".9" fill="#999"/></svg></span>
    Design-Modeling
  </div>
</div>

<div class="abs sec-title" style="top:762px"><h2>Our Services</h2><span class="track"></span></div>
<p class="abs intro" style="top:810px">Lorem Ipsum is simply dummy text of the printing and typesetting industry. Lorem Ipsum has been the industry's standard dummy text ever since the 1500s, when an unknown printer took a galley of type and scrambled it to make a type specimen book. It has survived not only five centuries, but also the leap into electronic typesetting, remaining essentially unchanged. It was popularised in the 1960s with the release of Pressline sheets containing Lorem Ipsum.</p>

<svg class="abs chev" style="left:146px;top:987px" viewBox="0 0 14 22"><path d="M12 2 3 11l9 9" fill="none" stroke="#ccc" stroke-width="3"/></svg>
<div class="abs svc" style="left:172px"><div class="photo" role="img" aria-label="Cranes over a building site" style="background:linear-gradient(160deg,#3d6fc2,#6f98d6 45%,#8a6d45)"></div><span>General Construction</span></div>
<div class="abs svc" style="left:390px"><div class="photo" role="img" aria-label="Stone family house at dusk" style="background:linear-gradient(170deg,#5d7db5,#8c8a82 45%,#3c4a2c)"></div><span>Residential Construction</span></div>
<div class="abs svc" style="left:608px"><div class="photo" role="img" aria-label="Workers on scaffolding" style="background:linear-gradient(170deg,#2d59b8,#4d78c9 50%,#8a5a4a)"></div><span>Temporary Buildings</span></div>
<div class="abs svc" style="left:825px"><div class="photo" role="img" aria-label="Commercial building under construction" style="background:linear-gradient(170deg,#1d3f96,#4c6fb8 45%,#a0866a)"></div><span>Commercial Construction</span></div>
<svg class="abs chev" style="left:1038px;top:987px" viewBox="0 0 14 22"><path d="M2 2l9 9-9 9" fill="none" stroke="#ccc" stroke-width="3"/></svg>

<div class="abs sec-title" style="top:1136px"><h2>About Us</h2><span class="track"></span></div>
<p class="abs intro" style="top:1178px">There are many variations of passages of Lorem Ipsum available, but the majority have suffered alteration in some form, by injected humour, or randomised words which don't look even slightly believable. If you are going to use a passage of Lorem Ipsum, you need to be sure there isn't anything embarrassing hidden in the middle of text. All the Lorem Ipsum generators on the Internet tend to repeat predefined chunks as necessary, making this the first true generator on the Internet. It uses a dictionary of over 200 Latin words, combined with a handful of model sentence structures, to generate Lorem Ipsum which looks reasonable. The generated Lorem Ipsum is therefore always free from repetition, injected humour, or non-characteristic words etc.</p>

<div class="abs feature" style="left:170px"><h3>Over 15 Years Experience</h3><p>We combine quality workmanship, superior knowledge and low prices to provide you with service unmatched by our competitors.</p></div>
<div class="abs feature" style="left:479px"><h3>Best Materials</h3><p>We have the experience, personel and resources to make the project run smoothly. We can ensure a job is done on time.</p></div>
<div class="abs feature" style="left:786px"><h3>Professional Standards</h3><p>Work with us involve a carefully planned series of steps, centered around a schedule we stick to and daily communication.</p></div>

<div class="abs sec-title" style="top:1397px"><h2>Recent Projects</h2><span class="track"></span></div>
<div class="abs band" role="img" aria-label="City skyline tinted in blue"></div>
<svg class="abs chev" style="left:146px;top:1602px" viewBox="0 0 14 22"><path d="M12 2 3 11l9 9" fill="none" stroke="#fff" stroke-width="3"/></svg>
<div class="abs proj" style="left:170px"><div class="photo" role="img" aria-label="Park with flowering trees and tulips" style="background:linear-gradient(170deg,#dfe6e8,#c3ccaa 45%,#9b8a78 80%,#c4586a)"></div><div class="frame"></div><h4>Park Gardens</h4></div>
<div class="abs proj" style="left:464px"><div class="photo" role="img" aria-label="Modern glass house at dusk" style="background:linear-gradient(170deg,#6f9fd6,#a9c0d8 40%,#b08a5a 70%,#6a5a4a)"></div><div class="frame"></div><h4>Glass House</h4></div>
<div class="abs proj" style="left:756px"><div class="photo" role="img" aria-label="Modern pavilion with a green roof" style="background:linear-gradient(170deg,#e4e9ec,#b8c3a8 45%,#7c8a58 75%,#9aa86a)"></div><div class="frame"></div><h4>Creative Architects</h4></div>
<svg class="abs chev" style="left:1040px;top:1602px" viewBox="0 0 14 22"><path d="M2 2l9 9-9 9" fill="none" stroke="#fff" stroke-width="3"/></svg>

<div class="abs cta">
  <span class="q">Have A Question? <u>Contact Us Now</u></span>
  <span class="btn-black">Client Portal</span>
</div>

<div class="abs sec-title" style="top:1905px"><h2>Contact Info</h2><span class="track"></span></div>
<div class="abs box info">
  <div>&#9742; Phone: (012)-555-0147</div>
  <div>
    <svg width="8" height="11" viewBox="0 0 8 11"><path d="M4 11 .6 5A3.6 3.6 0 1 1 7.4 5Z" fill="#222"/><circle cx="4" cy="3.7" r="1.3" fill="#fff"/></svg>
    Address: 48 Alder Lane,
  </div>
  <div>Fairmont 3100</div>
  <div>
    <svg width="11" height="8" viewBox="0 0 11 8"><rect x=".5" y=".5" width="10" height="7" fill="none" stroke="#222"/><path d="M.5 .5 5.5 4.5 10.5 .5" fill="none" stroke="#222"/></svg>
    Email: info@oakhavenbuild.com
  </div>
  <div class="socials"><span class="dot dark"></span><span class="dot dark"></span><span class="dot dark"></span><span class="dot dark"></span><span class="dot dark"></span></div>
</div>
<div class="abs box map" role="img" aria-label="Street map with a location pin near the office"></div>

<div class="abs field" style="left:810px;top:1962px;width:102px;height:21px">Name<i>*</i></div>
<div class="abs field" style="left:925px;top:1962px;width:102px;height:21px">E-mail<i>*</i></div>
<div class="abs field" style="left:810px;top:1991px;width:217px;height:23px">Subject<i>*</i></div>
<div class="abs field" style="left:810px;top:2023px;width:217px;height:94px">Message<i>*</i></div>
<div class="abs submit">Submit</div>

<footer class="abs footer">
  <nav><span class="active">Home</span><span>Roofing</span><span>Apartment</span><span>Client Portal</span><span>Contact Us</span></nav>
  <p>&copy; 2016 Copyright Oakhaven Construction (Pvt) Ltd. Allright reserved.</p>
</footer>

</body>
</html>
```